Business Card - Professional Minimalist - Double sided

We appreciate minimalist logo/web/collateral designs that allow design to tell a story. We want to relay a professional image/approach but throwing in a splash of modern when we’re able so long as it’s not distracting. Think 75% classic corporate, 25% modern. Open to black or white design, not sure which might look the best.

Target Market(s)

Senior executives or related government affairs contacts within the agriculture, energy, and defense industries (i.e., potential clients) but located outside of Washington, DC. Most potential clients based in DC with be familiar with both of us and our shared history.

Industry/Entity Type

Consulting

Contact Information for Business Card

Name: Daniel R. Whitlock
Title: Co-Founder & Partner
Address: 418 Bramblewood Ave. SE | Suite 2716 | Washington, D.C. 20019
Phone: (202) 555-0187
Email: Daniel@HollerbyWhitlock.com

Font styles to use
Serif

Colors

Designer to choose only greyscale colors for use in the design.

Requirements
Must have
• Name: Daniel R. Whitlock
Phone: (202) 555-0187

```html
<!DOCTYPE html>
<html lang="en">
<head>
<meta charset="utf-8">
<title>Hollerby Whitlock Group – Business Card</title>
<link href="https://fonts.googleapis.com/css2?family=Lato:wght@400;700&display=swap" rel="stylesheet">
<style>
  :root {
    --backdrop: #dcdcdc;
    --card: #161616;
    --ink-soft: #6e6e6e;
    --ink-mid: #8a8a8a;
    --ink-bright: #b4b4b4;
    --rule: #3c3c3c;
  }
  * { margin: 0; padding: 0; box-sizing: border-box; }
  html, body { width: 1200px; height: 900px; overflow: hidden; }
  body {
    background: var(--backdrop);
    font-family: "Lato", Arial, sans-serif;
    position: relative;
  }
  .card {
    position: absolute;
    left: 337px;
    width: 525px;
    height: 300px;
    background: var(--card);
    border-radius: 3px;
    box-shadow: 0 10px 24px rgba(0,0,0,0.18);
  }
  .card--front { top: 120px; }
  .card--back { top: 470px; }

  .brand {
    position: absolute;
    left: 78px;
    top: 132px;
    display: flex;
    align-items: center;
    gap: 16px;
  }
  .brand-mark {
    width: 30px;
    height: 30px;
    background: var(--ink-bright);
  }
  .brand-name {
    font-size: 22px;
    font-weight: 400;
    letter-spacing: 3px;
    text-transform: uppercase;
    color: var(--ink-bright);
  }

  .identity {
    position: absolute;
    right: 296px;
    top: 122px;
    text-align: right;
  }
  .identity-name {
    font-size: 22px;
    font-weight: 700;
    color: var(--ink-soft);
    line-height: 1.2;
  }
  .identity-title {
    font-size: 13px;
    color: var(--ink-soft);
    margin-top: 2px;
  }
  .divider {
    position: absolute;
    left: 258px;
    top: 84px;
    width: 1px;
    height: 132px;
    background: var(--rule);
  }
  .contact {
    position: absolute;
    left: 280px;
    top: 90px;
    font-size: 12px;
    line-height: 17px;
    color: var(--ink-mid);
    list-style: none;
  }
  .contact-line { display: flex; align-items: center; white-space: nowrap; }
  .contact-line--icon { padding-left: 0; }
  .contact-icon {
    width: 11px;
    height: 11px;
    margin-right: 8px;
    flex: none;
  }
  .contact-icon * { stroke: var(--ink-mid); fill: none; stroke-width: 1.4; }
  .contact-line--plain { padding-left: 19px; }
</style>
</head>
<body>
  <section class="card card--front" aria-label="Business card front">
    <div class="brand">
      <span class="brand-mark"></span>
      <span class="brand-name">Hollerby Whitlock Group</span>
    </div>
  </section>

  <section class="card card--back" aria-label="Business card back">
    <div class="identity">
      <p class="identity-name">Daniel R. Whitlock</p>
      <p class="identity-title">Co-Founder &amp; Partner</p>
    </div>
    <div class="divider"></div>
    <ul class="contact">
      <li class="contact-line contact-line--plain">418 Bramblewood Ave. SE</li>
      <li class="contact-line contact-line--plain">Suite 2716</li>
      <li class="contact-line contact-line--plain">Washington, D.C. 20019</li>
      <li class="contact-line contact-line--icon">
        <svg class="contact-icon" viewBox="0 0 12 12" aria-hidden="true">
          <path d="M3 1.5 L4.6 3.6 L3.6 4.8 Q4.6 7 7.2 8.4 L8.4 7.4 L10.5 9 L9.4 10.5 Q4.5 10 1.5 3 Z"/>
        </svg>
        (202) 555-0187
      </li>
      <li class="contact-line contact-line--icon">
        <svg class="contact-icon" viewBox="0 0 12 12" aria-hidden="true">
          <rect x="1" y="2.5" width="10" height="7"/>
          <path d="M1 2.5 L6 6.5 L11 2.5"/>
        </svg>
        Daniel@HollerbyWhitlock.com
      </li>
      <li class="contact-line contact-line--icon">
        <svg class="contact-icon" viewBox="0 0 12 12" aria-hidden="true">
          <circle cx="6" cy="6" r="4.8"/>
          <path d="M1.2 6 H10.8 M6 1.2 Q3.4 6 6 10.8 M6 1.2 Q8.6 6 6 10.8"/>
        </svg>
        www.HollerbyWhitlock.com
      </li>
    </ul>
  </section>
</body>
</html>
```